Design a business card and letterhead

Details:

• Trading Name : Valtrix
• Company Registration Number : 2014/583027/07
• Contact Name : Pieter Lombard – Professional Accountant
• Business Telephone Number : 0862 314 586
• Website Address : [login to view URL]
• Email Address : plombard@[login to view URL]
• Business Address : 47 Kestrel Road, Extension 8, Ridgeview
P.O. Box 653, Oak Terrace, 1057

```html
<!DOCTYPE html>
<html lang="en">
<head>
<meta charset="utf-8">
<title>Valtrix – Business Card</title>
<link rel="stylesheet" href="https://fonts.googleapis.com/css2?family=Open+Sans:ital,wght@0,400;0,600;1,400&display=swap">
<style>
  :root {
    --bg: #3a3a3a;
    --card: #ffffff;
    --ink: #1e1e1e;
    --blue: #2f6cc0;
    --band: #5f5f5f;
    --muted: #555555;
  }
  * { box-sizing: border-box; margin: 0; padding: 0; }
  html, body { width: 1200px; height: 900px; overflow: hidden; }
  body {
    background: var(--bg);
    font-family: "Open Sans", sans-serif;
    display: flex; flex-direction: column; align-items: center; justify-content: center;
    gap: 44px;
  }
  .card {
    position: relative; width: 660px; height: 377px;
    background: var(--card); border-radius: 18px; overflow: hidden;
  }
  .brand { display: flex; align-items: center; gap: 12px; }
  .brand-dot { width: 20px; height: 20px; border-radius: 50%; background: var(--blue); flex: none; }
  .brand-name { font-weight: 600; color: var(--ink); line-height: 1; }

  /* front */
  .card-front { display: flex; align-items: center; justify-content: center; }
  .card-front .brand-name { font-size: 50px; }

  /* back */
  .contact { position: absolute; left: 34px; top: 30px; }
  .person { display: flex; align-items: flex-start; gap: 10px; margin-bottom: 26px; }
  .person-name { color: var(--blue); font-size: 19px; font-weight: 600; letter-spacing: .5px; line-height: 1.1; }
  .person-role { font-style: italic; font-size: 11px; color: var(--muted); }
  .contact-row { display: flex; align-items: center; gap: 14px; margin-bottom: 16px; font-size: 12px; color: var(--ink); }
  .contact-row.address { align-items: flex-start; line-height: 1.5; }
  .icon { width: 22px; height: 22px; border-radius: 4px; background: var(--blue); flex: none; display: flex; align-items: center; justify-content: center; }
  .icon svg { width: 14px; height: 14px; fill: #fff; }
  .band { position: absolute; top: 0; bottom: 0; left: 450px; width: 110px; background: var(--band); }
  .logo-panel {
    position: absolute; left: 330px; top: 105px; width: 300px; height: 170px;
    background: var(--card); box-shadow: 0 6px 18px rgba(0,0,0,.25);
    display: flex; align-items: center; justify-content: center;
  }
  .logo-panel .brand-name { font-size: 38px; }
  .logo-panel .brand-dot { width: 16px; height: 16px; }
</style>
</head>
<body>
  <section class="card card-front" aria-label="Card front">
    <div class="brand"><span class="brand-dot"></span><span class="brand-name">Valtrix</span></div>
  </section>

  <section class="card card-back" aria-label="Card back">
    <div class="band"></div>
    <div class="contact">
      <div class="person">
        <span class="icon"><svg viewBox="0 0 16 16"><circle cx="8" cy="5" r="3"/><path d="M2 15c0-4 3-6 6-6s6 2 6 6z"/></svg></span>
        <div>
          <div class="person-name">PIETER LOMBARD</div>
          <div class="person-role">Professional Accountant</div>
        </div>
      </div>
      <div class="contact-row">
        <span class="icon"><svg viewBox="0 0 16 16"><path d="M4 1l2.5 3-1.5 2c1 2 3 4 5 5l2-1.5 3 2.5-2 2.5C7 14 2 9 1.5 3z"/></svg></span>
        <span>0862 314 586</span>
      </div>
      <div class="contact-row">
        <span class="icon"><svg viewBox="0 0 16 16"><path d="M1 8l14-6-4 13-3-5z"/></svg></span>
        <span>plombard@valtrix.co.za</span>
      </div>
      <div class="contact-row">
        <span class="icon"><svg viewBox="0 0 16 16"><path d="M6.5 9.5l3-3 1 1-3 3zM3 9l2-2 1 1-2 2a1.4 1.4 0 002 2l2-2 1 1-2 2a2.8 2.8 0 01-4-4zm10-2l-2 2-1-1 2-2a1.4 1.4 0 00-2-2L8 6 7 5l2-2a2.8 2.8 0 014 4z"/></svg></span>
        <span>www.valtrix.co.za</span>
      </div>
      <div class="contact-row address">
        <span class="icon"><svg viewBox="0 0 16 16"><path d="M8 1a5 5 0 00-5 5c0 4 5 9 5 9s5-5 5-9a5 5 0 00-5-5zm0 7a2 2 0 110-4 2 2 0 010 4z"/></svg></span>
        <span>47 Kestrel Road, Extension 8, Ridgeview<br>P.O. Box 653, Oak Terrace, 1057</span>
      </div>
    </div>
    <div class="logo-panel">
      <div class="brand"><span class="brand-dot"></span><span class="brand-name">Valtrix</span></div>
    </div>
  </section>
</body>
</html>
```